Cognitive therapist.

I am a therapist and my main work is with clients who have depression and anxiety disorders.

I need something reasonably plain. Cognitive therapy is a very pragmatic approach to dealing with problems, so it isn't new agey (no offence to new age therapies at all)

Hi everyone, I am currently looking at a particular design that I will most likely go with. Cheers, Lyn

Lyn Marchet
Cognitive Therapist
BA, PG Dip Mental Health,
PG Dip Cog Beh Therapy
MKRPG

The Quillan Rooms,
Level One
47 Harwick Parade
Cnr Drayfield St & Harwick Parade
P O Box 38 215
WELLINGTON 6287

Phone: 027 463 2851 Email: lmarchet@quorvane.co.nz

www.lynmarchet.co.nz

• No illustration, or colour. not old style fonts.

```html
<!DOCTYPE html>
<html lang="en">
<head>
<meta charset="utf-8">
<title>Lyn Marchet – Business Card</title>
<link rel="stylesheet" href="https://fonts.googleapis.com/css2?family=Lora:wght@400&family=Lato:wght@400&display=swap">
<style>
  :root {
    --backdrop: #e6e4e0;
    --card: #ffffff;
    --ink: #1f1f1f;
    --rule: #2a2a2a;
  }
  html, body {
    margin: 0;
    padding: 0;
    width: 1200px;
    height: 1023px;
    overflow: hidden;
    background: var(--backdrop);
  }
  .business-card {
    position: absolute;
    left: 120px;
    top: 236px;
    width: 960px;
    height: 550px;
    background: var(--card);
    box-shadow: 0 6px 24px rgba(0,0,0,0.18);
    color: var(--ink);
  }
  .card-name {
    position: absolute;
    left: 62px;
    top: 112px;
    margin: 0;
    font-family: "Lora", Georgia, serif;
    font-weight: 400;
    font-size: 66px;
    letter-spacing: 5px;
    line-height: 1;
    text-transform: uppercase;
  }
  .rule {
    position: absolute;
    left: 56px;
    width: 830px;
    height: 5px;
    background: var(--rule);
  }
  .rule--upper { top: 196px; }
  .rule--lower { top: 252px; }
  .card-credentials {
    position: absolute;
    left: 60px;
    top: 212px;
    margin: 0;
    font-family: "Lato", Arial, sans-serif;
    font-size: 21px;
    letter-spacing: 0.2px;
  }
  .contact-list {
    position: absolute;
    right: 540px;
    top: 372px;
    margin: 0;
    padding: 0;
    list-style: none;
    font-family: "Lato", Arial, sans-serif;
    font-size: 20px;
    line-height: 32px;
    text-align: right;
  }
  .contact-list li {
    display: flex;
    justify-content: flex-end;
    align-items: center;
    gap: 8px;
  }
  .contact-icon {
    width: 16px;
    height: 16px;
    flex: none;
  }
  .address {
    position: absolute;
    left: 470px;
    top: 372px;
    margin: 0;
    font-family: "Lato", Arial, sans-serif;
    font-style: normal;
    font-size: 20px;
    line-height: 32px;
  }
</style>
</head>
<body>
  <section class="business-card">
    <h1 class="card-name">Lyn Marchet</h1>
    <div class="rule rule--upper"></div>
    <p class="card-credentials">Cognitive Therapist BA, PG Dip Mental Health, PG Dip Cog Beh Therapy MKRPG</p>
    <div class="rule rule--lower"></div>

    <ul class="contact-list">
      <li>027 463 2851
        <svg class="contact-icon" viewBox="0 0 16 16" aria-hidden="true">
          <rect x="4" y="1" width="8" height="14" rx="1.5" fill="none" stroke="#1f1f1f" stroke-width="1.4"/>
          <line x1="7" y1="12.5" x2="9" y2="12.5" stroke="#1f1f1f" stroke-width="1.2"/>
        </svg>
      </li>
      <li>lmarchet@quorvane.co.nz
        <svg class="contact-icon" viewBox="0 0 16 16" aria-hidden="true">
          <rect x="1" y="3" width="14" height="10" fill="#1f1f1f"/>
          <polyline points="1,3 8,9 15,3" fill="none" stroke="#ffffff" stroke-width="1.2"/>
        </svg>
      </li>
      <li>www.lynmarchet.co.nz
        <svg class="contact-icon" viewBox="0 0 16 16" aria-hidden="true">
          <circle cx="8" cy="8" r="6.5" fill="none" stroke="#1f1f1f" stroke-width="1.4"/>
          <ellipse cx="8" cy="8" rx="2.8" ry="6.5" fill="none" stroke="#1f1f1f" stroke-width="1"/>
          <line x1="1.5" y1="8" x2="14.5" y2="8" stroke="#1f1f1f" stroke-width="1"/>
        </svg>
      </li>
    </ul>

    <address class="address">
      The Quillan Rooms, Level One<br>
      47 Harwick Parade Cnr Drayfield St &amp; Harwick Parade<br>
      P.O. Box 38 215 Wellington 6287
    </address>
  </section>
</body>
</html>
```